POLITICAL CARD TO HAND OUT

A LITTLE LARGER THAN THE REGULAR BUSINESS CARD WITH THE ABOVE INFORMATION.

Industry/Entity Type

Business

Contact Information for Business Card

ELECT *DEAN HOLT* FOR JUSTICE OF THE PEACE PCT 6-EXPERIENCED LEADERSHIP- WITH MY PICTURE ON IT- PHONE 347-610-2853-MERIDIAN PRIMARY - EARLY VOTING FEB 18TH THRU FEB 28 AND ELECTION DAY IS MARCH 4TH, 2014- USE RED WHITE AND BLUE WITH SOME STARS.

Requirements
Must have
• A FIVE POINTED STAR ON EACH SIDE OF MY NAME

```html
<!DOCTYPE html>
<html lang="en">
<head>
<meta charset="utf-8">
<title>Elect Dean Holt – Campaign Card</title>
<link rel="stylesheet" href="https://fonts.googleapis.com/css2?family=Archivo+Black&family=Roboto+Condensed:ital,wght@0,700;1,700;1,900&family=Roboto:wght@500&display=swap">
<style>
  :root {
    --page-bg: #e6e7ea;
    --card-white: #ffffff;
    --flag-blue: #1f5cc0;
    --flag-blue-light: #3f8fe3;
    --ribbon-navy: #26308a;
    --star-navy: #2a3796;
    --flag-red: #c4202c;
    --flag-red-light: #e24a4f;
    --accent-yellow: #f4e312;
    --ink: #222633;
    --photo-tone: #6a4c3d;
  }
  * { margin: 0; padding: 0; box-sizing: border-box; }
  html, body {
    width: 1000px;
    height: 1200px;
    overflow: hidden;
    background: var(--page-bg);
  }
  .campaign-card {
    position: absolute;
    left: 50px;
    top: 340px;
    width: 900px;
    height: 520px;
    box-shadow: 0 14px 34px rgba(0, 0, 0, 0.25);
  }
  .campaign-card svg { display: block; }
  .elect-label {
    font-family: "Roboto Condensed", sans-serif;
    font-style: italic;
    font-weight: 900;
    font-size: 34px;
    fill: var(--card-white);
    letter-spacing: 1px;
  }
  .candidate-name {
    font-family: "Archivo Black", sans-serif;
    font-size: 110px;
    fill: var(--card-white);
  }
  .phone-number {
    font-family: "Roboto Condensed", sans-serif;
    font-style: italic;
    font-weight: 700;
    font-size: 34px;
    fill: var(--card-white);
  }
  .office-line {
    font-family: "Roboto Condensed", sans-serif;
    font-weight: 700;
    font-size: 15px;
    fill: var(--card-white);
    letter-spacing: 0.5px;
  }
  .voting-dates {
    font-family: "Roboto", sans-serif;
    font-weight: 500;
    font-size: 15px;
    fill: var(--ink);
    letter-spacing: 0.3px;
  }
</style>
</head>
<body>
<div class="campaign-card">
  <svg width="900" height="520" viewBox="0 0 900 520" xmlns="http://www.w3.org/2000/svg">
    <defs>
      <radialGradient id="sky-blue" cx="0.55" cy="0.35" r="0.75">
        <stop offset="0" stop-color="var(--flag-blue-light)"/>
        <stop offset="1" stop-color="var(--flag-blue)"/>
      </radialGradient>
      <polygon id="star" points="0,-1 0.2245,-0.309 0.951,-0.309 0.3633,0.118 0.5878,0.809 0,0.382 -0.5878,0.809 -0.3633,0.118 -0.951,-0.309 -0.2245,-0.309"/>
    </defs>

    <!-- card base -->
    <rect class="card-base" width="900" height="520" fill="var(--card-white)"/>

    <!-- red and white sweep -->
    <path class="red-sweep" d="M0,300 C360,300 660,390 900,420 V470 C660,440 360,345 0,345 Z" fill="var(--flag-red)"/>
    <path class="white-stripe" d="M0,312 C360,312 660,402 900,432 V442 C660,412 360,322 0,322 Z" fill="var(--card-white)"/>
    <path class="red-highlight" d="M0,330 C360,330 660,420 900,450 V456 C660,426 360,336 0,336 Z" fill="var(--flag-red-light)"/>

    <!-- blue field -->
    <path class="blue-field" d="M0,0 H900 V420 C660,390 360,300 0,300 Z" fill="url(#sky-blue)"/>

    <!-- scattered small stars -->
    <g class="scatter-stars" fill="var(--star-navy)">
      <use href="#star" transform="translate(60,225) scale(11)"/>
      <use href="#star" transform="translate(95,262) scale(7)"/>
      <use href="#star" transform="translate(35,280) scale(8)"/>
      <use href="#star" transform="translate(140,295) scale(6)"/>
      <use href="#star" transform="translate(820,300) scale(8)"/>
      <use href="#star" transform="translate(860,340) scale(6)" opacity="0.7"/>
    </g>

    <!-- name-flanking stars -->
    <g class="name-stars" fill="none" stroke="var(--card-white)" stroke-linejoin="round">
      <use href="#star" transform="translate(62,170) scale(34)" stroke-width="0.12"/>
      <use href="#star" transform="translate(852,180) scale(34)" stroke-width="0.12"/>
    </g>
    <use class="accent-star" href="#star" transform="translate(455,55) scale(14)" fill="var(--card-white)"/>
    <use class="accent-star" href="#star" transform="translate(640,70) scale(15)" fill="var(--accent-yellow)"/>

    <!-- headline -->
    <text class="elect-label" x="132" y="100">ELECT</text>
    <text class="candidate-name" x="110" y="222" textLength="446" lengthAdjust="spacingAndGlyphs">DEAN H</text>
    <rect class="name-o-frame" x="560" y="140" width="86" height="84" rx="38" fill="var(--card-white)"/>
    <rect class="candidate-photo" x="570" y="150" width="66" height="64" rx="30" fill="var(--photo-tone)" role="img" aria-label="Portrait photograph of the candidate"/>
    <text class="candidate-name" x="650" y="222" textLength="150" lengthAdjust="spacingAndGlyphs">LT</text>

    <!-- ribbon -->
    <polygon class="ribbon-end-left" points="22,240 42,240 30,263 42,286 22,286 10,263" fill="var(--flag-red)"/>
    <polygon class="ribbon-end-right" points="858,240 878,240 890,263 878,286 858,286 870,263" fill="var(--flag-red)"/>
    <rect class="ribbon" x="38" y="240" width="824" height="46" fill="var(--ribbon-navy)"/>
    <line class="ribbon-divider" x1="450" y1="246" x2="450" y2="280" stroke="var(--flag-blue-light)" stroke-width="1.5"/>

    <!-- phone -->
    <g class="phone-icon" fill="none" stroke="var(--card-white)" stroke-width="2.5">
      <rect x="62" y="249" width="18" height="28" rx="3"/>
      <line x1="66" y1="255" x2="76" y2="255"/>
      <line x1="66" y1="262" x2="76" y2="262"/>
      <line x1="66" y1="269" x2="76" y2="269"/>
    </g>
    <text class="phone-number" x="92" y="276">347-610-2853</text>

    <!-- office -->
    <text class="office-line" x="650" y="259" text-anchor="middle">FOR JUSTICE OF THE PEACE PCT 6</text>
    <text class="office-line" x="650" y="278" text-anchor="middle">EXPERIENCED LEADERSHIP</text>

    <!-- voting dates -->
    <text class="voting-dates" x="540" y="482">MERIDIAN PRIMARY - EARLY VOTING</text>
    <text class="voting-dates" x="540" y="500">FEB 18TH THRU FEB 28 AND ELECTION DAY</text>
    <text class="voting-dates" x="540" y="518" dy="-2">IS MARCH 4TH, 2014</text>
  </svg>
</div>
</body>
</html>
```